Investment Company Business Card Design

We need a Business Card design for a new company based in Boston called "Velm Investment". We are cooperating with local real estate and construction companies. Our company is very actively and aggressively acquiring primarily residential investment properties either to buy and hold long term or for purposes or renovating and repositioning for re-sale in the market. In addition, we undertake some development projects and acquisitions as opportunities present themselves. the final design should contains information about “Velm" the river boat. we are tenacious, indomitable, and the business have a favorable wind throughout the voyage for all our investment.
sample Info. on Design:
Tusa Merrick
CEO
555-xxx-xxxx
418 Harlow St. Suite 507, Calden, VT 05091
Please provide a template also, that we can edit the info later.
Reason: i just got new LOGO Design attached will be use in Business Card Design.
Construction

```html
<!DOCTYPE html>
<html lang="en">
<head>
<meta charset="utf-8">
<title>Velm Investment – Business Card</title>
<link rel="stylesheet" href="https://fonts.googleapis.com/css2?family=Open+Sans:wght@400;600&display=swap">
<style>
  :root {
    --backdrop: #3a2414;
    --card-dark: #231f20;
    --card-light: #ffffff;
    --gold: #c9a24a;
    --gold-light: #f0d98c;
    --gold-deep: #a9802f;
    --ink: #3a3a3a;
    --mist: #e3e3e3;
    --on-dark: #e8e8e8;
  }
  * { margin: 0; padding: 0; box-sizing: border-box; }
  html, body { width: 1200px; height: 750px; overflow: hidden; }
  body {
    background: var(--backdrop);
    font-family: "Open Sans", Arial, sans-serif;
    position: relative;
  }
  .card {
    position: absolute;
    left: 330px;
    width: 541px;
    box-shadow: 0 6px 18px rgba(0,0,0,.45);
  }
  .card--front {
    top: 40px;
    height: 332px;
    background: var(--card-dark);
    display: flex;
    align-items: center;
    justify-content: center;
  }
  .card--back {
    top: 382px;
    height: 333px;
    background: var(--card-dark);
  }
  .brand-name {
    font-weight: 600;
    color: var(--gold);
    letter-spacing: 1px;
    white-space: nowrap;
  }
  .card--front .brand-name { font-size: 30px; }
  .card--back .brand-name {
    position: absolute;
    left: 308px;
    top: 234px;
    font-size: 20px;
  }
  .back-top {
    position: absolute;
    inset: 0 0 auto 0;
    height: 186px;
    background: var(--card-light);
  }
  .emblem-area {
    position: absolute;
    left: 12px;
    top: 22px;
    width: 236px;
    height: 152px;
    background: linear-gradient(160deg, var(--mist), #f4f4f4);
    border-radius: 0 0 120px 10px;
  }
  .gold-rule {
    position: absolute;
    top: 186px;
    left: 0;
    right: 0;
    height: 6px;
    background: linear-gradient(90deg, var(--gold-deep), var(--gold-light) 50%, var(--gold-deep));
  }
  .contact-list {
    position: absolute;
    left: 315px;
    top: 55px;
    list-style: none;
    font-size: 11px;
    color: var(--ink);
  }
  .contact-list li {
    display: flex;
    align-items: center;
    gap: 10px;
    height: 22px;
  }
  .contact-list .role-row { margin-bottom: 22px; }
  .contact-list .phone-row { margin-bottom: 6px; }
  .badge {
    width: 23px;
    height: 20px;
    display: flex;
    align-items: center;
    justify-content: center;
    background: var(--card-dark);
  }
  .badge--role {
    background: linear-gradient(135deg, var(--gold-light), var(--gold-deep));
    color: var(--card-dark);
    font-size: 8px;
    font-weight: 600;
  }
  .address {
    position: absolute;
    left: 38px;
    top: 232px;
    display: flex;
    gap: 10px;
    color: var(--on-dark);
    font-size: 12.5px;
    line-height: 19px;
  }
  .address svg { margin-top: 3px; }
</style>
</head>
<body>
  <section class="card card--front">
    <span class="brand-name">Velm Investment</span>
  </section>

  <section class="card card--back">
    <div class="back-top">
      <div class="emblem-area" role="img" aria-label="Faint brand emblem decoration"></div>
      <ul class="contact-list">
        <li class="role-row"><span class="badge badge--role">CEO</span>TUSA MERRICK</li>
        <li class="phone-row">
          <span class="badge">
            <svg width="10" height="10" viewBox="0 0 24 24"><path fill="#fff" d="M6.6 10.8a15.1 15.1 0 0 0 6.6 6.6l2.2-2.2c.3-.3.7-.4 1-.2 1.1.4 2.3.6 3.6.6.6 0 1 .4 1 1V20c0 .6-.4 1-1 1A17 17 0 0 1 3 4c0-.6.4-1 1-1h3.5c.6 0 1 .4 1 1 0 1.3.2 2.5.6 3.6.1.3 0 .7-.2 1z"/></svg>
          </span>555-000-000
        </li>
        <li>
          <span class="badge">
            <svg width="11" height="9" viewBox="0 0 22 16"><rect x="1" y="1" width="20" height="14" fill="none" stroke="#fff" stroke-width="2"/><path d="M1 1l10 8 10-8" fill="none" stroke="#fff" stroke-width="2"/></svg>
          </span>hello@velmmail.com
        </li>
      </ul>
    </div>
    <div class="gold-rule"></div>
    <div class="address">
      <svg width="9" height="12" viewBox="0 0 12 16"><path fill="#fff" d="M6 0a6 6 0 0 0-6 6c0 4.5 6 10 6 10s6-5.5 6-10a6 6 0 0 0-6-6zm0 8.5A2.5 2.5 0 1 1 6 3.5a2.5 2.5 0 0 1 0 5z"/></svg>
      <p>418 Harlow St. Suite 507,<br>Calden, VT 05091</p>
    </div>
    <span class="brand-name">Velm Investment</span>
  </section>
</body>
</html>
```